" 816 " PACKAGING FOR AUTOMOTIVE SPAREPARTS PRODUCT

We need a zipped plastic packaging design for our product (i attached plastic packaging sample from another product). The plastic size is 40cm (length) * 30cm (width) with zipped on upside.

Our product is rubber parts for car suspension application. The brand is 816 and the slogan is 816 ORIGINAL PARTS ( see attached file).

We prefer the design use mostly red color (same color as our logo) and combine with other attracting color and it is on your control.
I have included a picture of packaging box that we currently use.

On the front side of the plastic packaging should have a view window that can view and see through the product inside the packaging.

The color and the design is on your control.
Updates

Project Deadline Extended
Reason: Hi I extend the deadline, create your Best design..

Target Market(s)

All customers, car workshop, retailer and user.

Industry/Entity Type

Automotive

Requirements
Must have
• - A space for labeling on front side of the packaging. (label size 4cm (lenght) * 7cm (width).
• - Should have the Pictures of our product on the packaging. I have included some pictures of our product, You can choose and put some of the pictures on the packaging.
• - The design should can communicate HIGH QUALITY PARTS.
Nice to have
• - Have some Blue print or silhouette (with a bit transparancy) of car spareparts item or workshop tool kit on the design.

```html
<!DOCTYPE html>
<html lang="en">
<head>
<meta charset="utf-8">
<title>816 Original Parts – Pouch Front</title>
<link rel="stylesheet" href="https://fonts.googleapis.com/css2?family=Oswald:wght@300;700&family=Montserrat:wght@700&display=swap">
<style>
  :root {
    --backdrop: #ebe9d6;
    --navy-deep: #12125a;
    --navy: #22268c;
    --space-blue: #1f4fb0;
    --space-glow: #3fb4e6;
    --brand-red: #e8202a;
    --brand-red-dark: #b5121b;
    --ribbon-blue: #3a97cf;
    --ribbon-light: #6cc3e8;
    --gear-grey: #d9dbe0;
    --white: #ffffff;
  }
  html, body {
    margin: 0;
    padding: 0;
    width: 1200px;
    height: 1020px;
    overflow: hidden;
    background: var(--backdrop);
  }
  .canvas {
    position: relative;
    width: 1200px;
    height: 1020px;
    background: var(--backdrop);
  }
  .pouch-front {
    position: absolute;
    left: 300px;
    top: 80px;
    width: 600px;
    height: 860px;
  }
  .brand-name {
    font-family: "Oswald", sans-serif;
    font-weight: 700;
    fill: var(--brand-red);
  }
  .brand-tagline {
    font-family: "Oswald", sans-serif;
    font-weight: 300;
    fill: var(--white);
  }
  .ribbon-text {
    font-family: "Montserrat", sans-serif;
    font-weight: 700;
    fill: var(--white);
  }
  .window-mark {
    font-family: "Oswald", sans-serif;
    font-weight: 700;
    fill: var(--white);
    fill-opacity: 0.75;
  }
</style>
</head>
<body>
<main class="canvas">
  <svg class="pouch-front" viewBox="0 0 600 860" xmlns="http://www.w3.org/2000/svg">
    <defs>
      <linearGradient id="pouchBody" x1="0" y1="0" x2="0" y2="1">
        <stop offset="0" stop-color="var(--navy-deep)"/>
        <stop offset="1" stop-color="var(--navy)"/>
      </linearGradient>
      <radialGradient id="spacePanel" cx="0.45" cy="0.35" r="0.75">
        <stop offset="0" stop-color="var(--space-glow)"/>
        <stop offset="0.45" stop-color="var(--space-blue)"/>
        <stop offset="1" stop-color="var(--navy-deep)"/>
      </radialGradient>
      <linearGradient id="ribbonFill" x1="0" y1="0" x2="1" y2="0">
        <stop offset="0" stop-color="var(--ribbon-blue)"/>
        <stop offset="0.5" stop-color="var(--ribbon-light)"/>
        <stop offset="1" stop-color="var(--ribbon-blue)"/>
      </linearGradient>
      <linearGradient id="windowFill" x1="0" y1="0" x2="0" y2="1">
        <stop offset="0" stop-color="#f0606a"/>
        <stop offset="1" stop-color="var(--brand-red-dark)"/>
      </linearGradient>
      <path id="ribbonLineTop" d="M80 648 Q300 690 530 622"/>
      <path id="ribbonLineBottom" d="M100 690 Q300 728 520 664"/>
    </defs>

    <!-- pouch body -->
    <rect class="pouch-body" x="0" y="0" width="600" height="860" rx="14" fill="url(#pouchBody)"/>

    <!-- zip seal lines -->
    <g class="zip-seal" stroke="#5a63c8" stroke-width="1.5" opacity="0.8">
      <line x1="0" y1="30" x2="600" y2="30"/>
      <line x1="0" y1="38" x2="600" y2="38"/>
      <line x1="0" y1="46" x2="600" y2="46"/>
      <line x1="0" y1="54" x2="600" y2="54"/>
      <line x1="0" y1="62" x2="600" y2="62"/>
    </g>

    <!-- tear notches -->
    <circle class="tear-notch" cx="0" cy="105" r="9" fill="var(--backdrop)"/>
    <circle class="tear-notch" cx="600" cy="105" r="9" fill="var(--backdrop)"/>

    <!-- front panel -->
    <rect class="front-panel" x="42" y="90" width="520" height="770" rx="20" fill="url(#spacePanel)"/>

    <!-- brand block -->
    <text class="brand-name" x="78" y="190" font-size="72">816</text>
    <text class="brand-tagline" x="78" y="370" font-size="26">816 Original Parts</text>

    <!-- product imagery -->
    <rect class="product-art" role="img" aria-label="Three white gear wheels illustrating car spare parts"
          x="290" y="130" width="272" height="420" rx="30" fill="var(--gear-grey)" opacity="0.85"/>

    <!-- red base band -->
    <rect class="red-band" x="0" y="680" width="600" height="180" rx="0" fill="var(--brand-red)"/>
    <rect class="red-band-corner" x="0" y="840" width="600" height="20" rx="14" fill="var(--brand-red)"/>

    <!-- see-through window -->
    <rect class="view-window" role="img" aria-label="Clear window showing red rubber suspension parts inside the pouch"
          x="55" y="700" width="490" height="150" rx="60" fill="url(#windowFill)" opacity="0.9"/>
    <text class="window-mark" x="300" y="830" font-size="110" text-anchor="middle">816</text>

    <!-- quality ribbon -->
    <path class="quality-ribbon" d="M50 612 Q300 668 560 590 L560 668 Q300 748 50 690 Z"
          fill="url(#ribbonFill)" opacity="0.95"/>
    <text class="ribbon-text" font-size="24" text-anchor="middle">
      <textPath href="#ribbonLineTop" startOffset="50%">HIGH QUALITY AUTO PARTS</textPath>
    </text>
    <text class="ribbon-text" font-size="24" text-anchor="middle">
      <textPath href="#ribbonLineBottom" startOffset="50%">816 ORIGINAL PARTS</textPath>
    </text>
  </svg>
</main>
</body>
</html>
```